Vegan Mobile Food Truck and Catering Flyers

We need a flyer designed as a promotional tool to give a bit of information about what we do, why we do it and our points of contact. It needs to be edgy and eye catching with a point of difference.

We are a mobile food truck serving Greek vegan food at major festivals and events around Adelaide. We offer catering services for private functions such as weddings and birthdays.

Veganism is the largest social justice movement that is striving to bring about a world where animals are not exploited for food, clothing, entertainment or any other purpose. We are vegan because we believe in equality for all life forms. We don't discriminate people by their race, nor animals by their species. Cats and dogs/cows and pigs.... the only difference is perspective. The will to live and right to freedom should not be determined by humans inconsistent contradictions.

There are only 5 reasons humans eat animal products and one of them is NOT necessity. They are culture, tradition, habit, taste and convenience. We are in an age of abundant information and technology, we must evolve to suit our current reality than live in the shadow of prehistoric ideologies that no longer serve us. The information is available. We once believed that black man belonged to serve the white man because of the colour of his skin. We now understand how ludicrous that is. There will come a time we look back on our perception of animals merely due to their species and think... that's insane. Speciesism is rife in our culture today but slowly people are realising the injustice that cannot be ignored.

We abstain from the use of animal products firstly and most importantly to avoid contributing to the senseless cruelty that the production of these products (that we simply do not need to live healthfully, create). Because of the environmental damage that is devastating our planet due to the resources required for production. Because animal products are toxic and unhealthy for our bodies to digest being the root cause to many of our largest health issues. Because it has been proven that there is enough food on earth to feed every last man, woman, and child. Yet people around the world continue to starve because the majority of crops (including those grown in countries where people are starving) are fed to livestock for affluent nations, and since the amount of animal-based food produced by the farming industry is much less than the amount of plant food put into it, there is a “diminished return on the investment,” the food supply dwindles, and humans end up going hungry.

A change in habit affects demand and demand affects supply. It is the only thing that will create an impact. Our choices do make a difference.

This is the message we want to convey without the essay of words.
We stand for compassion for all and when we know better we do better. We want to help people see, through our dishes, that you don't need to eat animal products to have a tasty satisfying meal. We want to share our knowledge and educate others.

Attached is our logo, tag line and contact details.

Perhaps even a reference saying, want to give vegan a go and see how easy it is to live a cruelty free lifestyle. Free with unlimited support and resources throughout the 22 days please visit https://www.trialmonth.example/trialmonth/
Also visit our website, read our blog to get a feel for the image of the business.

Below some links so you get the gist of the movement
http://gentleworld.org/tag/why-vegan/https://www.vegansociety.com/go-vegan/why-go-veganhttp://vegankit.com/why/http://www.plantfolkunion.example/why_vegan

To have more time to get this right as the designs are not what i had in mind and im not in a rush

Target Market(s)

our customers, both sexes, ages 17-65, foodies, open minded people

Industry/Entity Type

Food Service

Font styles to use
Sans Serif

Colors
fbca95
faa54b
cadf82
add136
ffffff
86cae7

Requirements
Must have
• information on why brivo and kin are vegan as explained in project description and in links provided. Also word document attached with some additional facts and figures which I am in the process of updating as I want Aussie stats and the most recent research.
• Include resources like 30 day trial on more information how to go vegan for those who may be interested to follow up.
• What brivo and kin do (without giving it a heading) and how to contact them to book events or follow them on social media to know where the food truck will be.
• double sided flyer
• attached are random pics of designs and styles and colours i like
Nice to have
• A bit of information on the food we serve, yiros and moussaka and greek style slaw. Newest addition to the menu is a street food type dish being loaded fries which is topped with our home made tzatziki and slaw.
Should not have
• no conservative professional looking flyers. i have attached some more that i like the idea of.
• i have now attached even more examples of what i like and don't like so that the concept is very clear.

```html
<!DOCTYPE html>
<html lang="en">
<head>
<meta charset="utf-8">
<title>Vegan food truck flyer</title>
<link rel="stylesheet" href="https://fonts.googleapis.com/css2?family=Roboto+Condensed:ital,wght@1,400;1,500;1,700&display=swap">
<style>
  :root {
    --backdrop: #c6bba4;
    --paper-edge: #e8cf9f;
    --paper: #7a7358;
    --ink: #1e1a12;
    --quote-card: #ebcf9e;
    --lettering: #ecd2a2;
    --art-light: #8a8268;
    --art-dark: #2a251b;
  }
  * { margin: 0; padding: 0; box-sizing: border-box; }
  html, body {
    width: 1200px; height: 700px; overflow: hidden;
    background: var(--backdrop);
    font-family: "Roboto Condensed", "Arial Narrow", sans-serif;
    color: var(--ink);
  }
  .flyer {
    position: absolute; left: 212px; top: 0;
    width: 776px; height: 650px;
    background: var(--paper-edge);
  }
  .flyer-panel {
    position: absolute; left: 19px; top: 0;
    width: 741px; height: 636px;
    background: var(--paper);
    overflow: hidden;
  }
  .intro {
    position: absolute; left: 31px; top: 2px;
    font-style: italic; font-weight: 500;
    font-size: 16px; line-height: 20.3px;
    letter-spacing: .45px;
    white-space: nowrap;
    z-index: 2;
  }
  .intro p + p { margin-top: 20.3px; }
  .headline {
    position: absolute; left: 362px; top: -22px;
    width: 380px;
    color: var(--lettering);
    font-style: italic; font-weight: 700;
    line-height: .9;
    transform: rotate(-14deg);
    transform-origin: left top;
    z-index: 1;
  }
  .headline-line { display: block; }
  .headline-line-main { font-size: 84px; }
  .headline-line-sub { font-size: 68px; text-align: right; padding-right: 10px; }
  .animal-art {
    position: absolute; left: 284px; top: 128px;
    width: 457px; height: 362px;
    background: radial-gradient(ellipse at 45% 55%, var(--art-light) 0%, var(--art-dark) 100%);
    border-radius: 45% 45% 20% 20%;
  }
  .quote-card {
    position: absolute; left: 36px; top: 395px;
    width: 298px; height: 89px;
    background: var(--quote-card);
    padding: 7px 8px 0;
    text-align: center;
    font-style: italic; font-weight: 500;
    font-size: 15px; line-height: 19px;
    letter-spacing: .25px;
    z-index: 2;
  }
  .rule {
    position: absolute; left: 31px; top: 493px;
    width: 688px; height: 2px; background: var(--ink);
  }
  .footnote {
    position: absolute; top: 509px; width: 336px;
    font-style: italic; font-weight: 500;
    font-size: 14px; line-height: 17px;
    letter-spacing: .2px;
    text-transform: uppercase;
  }
  .footnote-left { left: 47px; }
  .footnote-right { left: 386px; }
  .divider {
    position: absolute; left: 378px; top: 507px;
    width: 2px; height: 71px; background: var(--ink);
  }
  .social {
    position: absolute; left: 0; top: 594px; width: 741px;
    display: flex; justify-content: center; gap: 10px;
    list-style: none;
    font-style: italic; font-weight: 500; font-size: 16px; line-height: 24px;
    letter-spacing: .2px;
  }
  .social li { display: flex; align-items: center; gap: 3px; }
  .social-dot {
    width: 23px; height: 23px; border-radius: 50%;
    background: var(--ink); border: 2px solid #4a4434;
  }
</style>
</head>
<body>
  <main class="flyer">
    <section class="flyer-panel">
      <div class="intro">
        <p>reasonable price.</p>
        <p>Our commitment is to care for the welfare<br>
        of all animals and the environment.<br>
        All our meals are made without the use of any animal<br>
        products, inclusive of meat, milk, cheese, butter, cream<br>
        and eggs. Our ingredients<br>
        are 100% plant based. We are c<br>
        onfident we can change any<br>
        preconception you may have that<br>
        being vegan is limiting.</p>
        <p>We offer yiros and moussaka<br>
        and greek style slaw.<br>
        Newest addition to the menu<br>
        is a street food type dish being<br>
        loaded fries which is topped<br>
        with our home made tzatziki<br>
        and slaw.</p>
      </div>

      <h1 class="headline">
        <span class="headline-line headline-line-main">difference</span>
        <span class="headline-line headline-line-sub">do you?</span>
      </h1>

      <div class="animal-art" role="img" aria-label="Illustration of an animal head split down the middle, half dog and half tagged calf"></div>

      <blockquote class="quote-card">“If it is wrong to act violently to a dog or cat just for enjoyment or convenience, how can we justify the horrible things we do to other animals?”</blockquote>

      <div class="rule"></div>
      <p class="footnote footnote-left">Lorem ipsum dolor sit amet, consectetuer adipiscing elit, sed diam nonummy nibh euismod tincidunt ut laoreet dolore magna aliquam erat volutpat.</p>
      <div class="divider"></div>
      <p class="footnote footnote-right">Lorem ipsum dolor sit amet, consectetuer adipiscing elit, sed diam nonummy nibh euismod tincidunt ut laoreet dolore magna aliquam erat volutpat.</p>

      <ul class="social">
        <li><span class="social-dot"></span>@CompanyName</li>
        <li><span class="social-dot"></span>@CompanyName</li>
        <li><span class="social-dot"></span>@CompanyName</li>
      </ul>
    </section>
  </main>
</body>
</html>
```